3D Printing Business coming soon page

Hi we are looking for a one page "coming soon" website for our business. The business is called "Strideform Labs" and it is a new solution which 3D Prints Orthotics (Insoles).

The design should include our logo, an improved version of our promotional image (attached), a web form for capturing interest from people, a countdown timer and some text.

Follow the colour scheme which is shown in our logo along with our other colours - Orange (RGB#ff8300) and Light Green (RGB#30f20a)
Updates

Industry/Entity Type

Business

Font styles to use
Sans Serif

Requirements
Must have
• Logo (Attached)
Improved version of Promotional Image
Web Form design for capturing Name, EMail Address and Comments along with a Turin test
Countdown Timer
Text - "Strideform Labs will shake up the Orthotics Industry. Foot Orthosis patient-ready in hours for a fraction of the price you are paying today. Welcome to the new world of 3D Printing!"

Files

```html
<!DOCTYPE html>
<html lang="en">
<head>
<meta charset="utf-8">
<title>Strideform Labs – Coming Soon</title>
<link rel="stylesheet" href="https://fonts.googleapis.com/css2?family=Oswald:wght@300;400;500;700&display=swap">
<style>
  :root {
    --sky-top: #3f5f9e;
    --sky-mid: #9fb3cf;
    --earth: #8a5a3a;
    --road: #4a4c52;
    --road-dark: #2e3036;
    --title-green: #30f20a;
    --arrow-green: #1a9a3e;
    --header-green: #2e8b3e;
    --panel-navy: #243a79;
    --digit-navy: #1f3f73;
    --label-blue: #1c4e8a;
    --white: #ffffff;
    --field-text: #8a8f99;
    --captcha-red: #8b1a10;
    --submit-top: #5cf23a;
    --submit-bottom: #22b418;
    --logo-blue: #1f6fb5;
  }
  * { box-sizing: border-box; margin: 0; padding: 0; }
  html, body { width: 1200px; height: 798px; overflow: hidden; }
  body { font-family: 'Oswald', sans-serif; position: relative; }

  .backdrop {
    position: absolute; inset: 0;
    background: linear-gradient(180deg, var(--sky-top) 0%, var(--sky-mid) 30%, #c9cdd2 40%, var(--earth) 46%, #6b5a4a 52%, var(--road) 62%, var(--road-dark) 100%);
  }

  .page-title {
    position: absolute; left: 391px; top: 20px; width: 400px;
    white-space: nowrap; text-align: center;
    font-weight: 700; font-size: 46px; line-height: 60px; letter-spacing: -1px;
    color: var(--title-green); text-shadow: 2px 3px 4px rgba(0,0,0,.45);
  }

  .countdown-box {
    position: absolute; left: 121px; top: 114px; width: 691px; height: 277px;
    border: 1px solid rgba(255,255,255,.7); border-top-color: var(--title-green);
  }
  .timer { position: absolute; top: 62px; left: 0; width: 100%; }
  .timer-unit { position: absolute; width: 140px; margin-left: -70px; text-align: center; }
  .timer-digits {
    display: block; font-weight: 700; font-size: 74px; line-height: 76px;
    color: var(--digit-navy); text-shadow: 0 2px 3px rgba(255,255,255,.3);
  }
  .timer-label { display: block; font-weight: 400; font-size: 18px; color: var(--label-blue); margin-top: 10px; }
  .tagline {
    position: absolute; left: 38px; right: 38px; top: 220px;
    text-align: center; color: var(--white); font-weight: 300; font-size: 17px; line-height: 22px;
  }

  .contact-panel {
    position: absolute; left: 820px; top: 25px; width: 273px; height: 366px;
    background-color: var(--panel-navy);
    background-image: linear-gradient(rgba(255,255,255,.05) 1px, transparent 1px), linear-gradient(90deg, rgba(255,255,255,.05) 1px, transparent 1px);
    background-size: 4px 4px;
    box-shadow: 0 0 4px rgba(0,0,0,.4);
  }
  .contact-header {
    height: 64px; background: var(--header-green);
    color: var(--white); font-size: 31px; font-weight: 400; text-align: center; line-height: 64px;
    letter-spacing: 1px;
  }
  .field {
    position: absolute; left: 14px; width: 245px; background: var(--white);
    color: var(--field-text); font-size: 11px; font-weight: 300; letter-spacing: .5px; padding: 6px 10px;
  }
  .field-email { top: 78px; height: 28px; }
  .field-message { top: 117px; height: 112px; }
  .captcha {
    position: absolute; left: 45px; top: 239px; width: 183px; height: 71px;
    background: linear-gradient(180deg, #f4f4f4 0 50%, #efd98a 50% 100%);
    border: 3px solid var(--captcha-red);
  }
  .submit {
    position: absolute; left: 58px; top: 321px; width: 151px; height: 32px;
    background: linear-gradient(180deg, var(--submit-top), var(--submit-bottom));
    color: var(--white); font-weight: 700; font-size: 20px; text-align: center; line-height: 32px;
  }

  .step-label { position: absolute; width: 220px; margin-left: -110px; text-align: center; color: var(--white); font-weight: 300; font-size: 20px; white-space: nowrap; }
  .step-photo { position: absolute; }
  .photo-fit { left: 203px; top: 469px; width: 224px; height: 126px; background: linear-gradient(135deg, #1a1a1a 0%, #3b3b3b 40%, #d9c4a8 60%, #1c1c1c 100%); }
  .photo-scan { left: 870px; top: 466px; width: 124px; height: 129px; background: linear-gradient(180deg, #2b2b2b 0 15%, #d8d8dc 15% 100%); }
  .photo-design { left: 715px; top: 643px; width: 194px; height: 109px; background: linear-gradient(135deg, #f4f6f8 0%, #e8b8a4 50%, #f4f6f8 100%); }
  .photo-print { left: 405px; top: 636px; width: 154px; height: 121px; background: linear-gradient(180deg, #b8304a 0 20%, #9fd8ec 20% 70%, #e6e4de 70% 100%); }

  .brand-mark { position: absolute; left: 527px; top: 480px; width: 200px; text-align: center; }
  .brand-dot { width: 60px; height: 60px; border-radius: 50%; background: var(--logo-blue); margin: 0 auto 8px; }
  .brand-name { font-weight: 700; font-size: 26px; color: var(--logo-blue); line-height: 30px; white-space: nowrap; }

  .flow-arrows { position: absolute; left: 0; top: 0; }
</style>
</head>
<body>
  <div class="backdrop" role="img" aria-label="Blurred photo of an open desert road under a blue sky"></div>

  <h1 class="page-title">Comming Soon</h1>

  <section class="countdown-box">
    <div class="timer">
      <div class="timer-unit" style="left:166px"><span class="timer-digits">000</span><span class="timer-label">Days</span></div>
      <div class="timer-unit" style="left:306px"><span class="timer-digits">00</span><span class="timer-label">Hours</span></div>
      <div class="timer-unit" style="left:425px"><span class="timer-digits">00</span><span class="timer-label">Minutes</span></div>
      <div class="timer-unit" style="left:544px"><span class="timer-digits">00</span><span class="timer-label">Seconds</span></div>
    </div>
    <p class="tagline">Strideform Labs will shake up the Orthotics Industry. Foot Orthosis patient-ready in hours for a fraction of the price you are paying today. Welcome to the new world of 3D Printing!</p>
  </section>

  <aside class="contact-panel">
    <h2 class="contact-header">CONTACT US</h2>
    <div class="field field-email">Email Address</div>
    <div class="field field-message">Text Your Message</div>
    <div class="captcha" role="img" aria-label="Two-word verification challenge with input box"></div>
    <div class="submit">SUBMIT</div>
  </aside>

  <svg class="flow-arrows" width="1200" height="798" viewBox="0 0 1200 798" aria-hidden="true">
    <polygon points="870,580 985,601 916,631" fill="var(--arrow-green)"/>
    <polygon points="665,652 665,769 621,710" fill="var(--arrow-green)"/>
    <polygon points="310,650 419,609 347,588" fill="var(--arrow-green)"/>
  </svg>

  <div class="step-label" style="left:289px; top:440px">4. Fit It</div>
  <div class="step-photo photo-fit" role="img" aria-label="Hands placing a custom insole into a black shoe"></div>

  <div class="brand-mark">
    <div class="brand-dot"></div>
    <div class="brand-name">Strideform Labs</div>
  </div>

  <div class="step-label" style="left:932px; top:440px">1. Scan The Foot</div>
  <div class="step-photo photo-scan" role="img" aria-label="Tablet fitted with a 3D foot scanner"></div>

  <div class="step-label" style="left:806px; top:607px">2. Design The Orthotic</div>
  <div class="step-photo photo-design" role="img" aria-label="Orthotic design software showing a foot model and insole"></div>

  <div class="step-label" style="left:487px; top:607px">3. 3D Print</div>
  <div class="step-photo photo-print" role="img" aria-label="Desktop 3D printer with red top and clear enclosure"></div>
</body>
</html>
```